New Company Business Card Design

I have a new company logo and I want a new business card design. I dont know if the logo file i attached is in the correct format or quality. We are a New York City Specialty construction Firm specializing in high risk out of the box projects. I want a simple and classy business card that people will his card is as crisp as the work his company does.

Target Market(s)

Clients in the heavy construction industry in New York City

Industry/Entity Type

Construction Company

Contact Information for Business Card

Simple Classy - DIFFERENT

Font styles to use
Other font styles liked:
• Mach the logo font in some way

Colors

Designer to choose colors to be used in the design.

Requirements
Must have
• Uniqueness
Nice to have
• Nothing particular - Just different and classy - Timeless
Should not have
• Goofy Shit or Gimmicky shit

```html
<!DOCTYPE html>
<html lang="en">
<head>
<meta charset="utf-8">
<title>Korvan Builders – Business Card</title>
<link href="https://fonts.googleapis.com/css2?family=Work+Sans:wght@400;500;800&display=swap" rel="stylesheet">
<style>
  :root {
    --backdrop: #2a2a2c;
    --card: #161617;
    --card-edge: #222224;
    --silver: #d9d9d9;
    --silver-soft: #b4b4b4;
    --muted: #8c8c8c;
    --rule: #5a5a5a;
  }
  * { margin: 0; padding: 0; box-sizing: border-box; }
  html, body {
    width: 1200px; height: 900px; overflow: hidden;
    background: var(--backdrop);
    font-family: "Work Sans", Arial, sans-serif;
  }
  .canvas {
    position: relative; width: 1200px; height: 900px;
  }
  .card {
    position: absolute; left: 260px; width: 680px; height: 389px;
    background: linear-gradient(135deg, var(--card-edge) 0%, var(--card) 60%);
    border-radius: 3px;
    box-shadow: 0 10px 30px rgba(0,0,0,.45);
  }
  .card--front { top: 50px; display: flex; align-items: center; justify-content: center; }
  .card--back { top: 470px; display: flex; align-items: center; }

  .wordmark {
    font-weight: 800; color: var(--silver);
    text-transform: uppercase; line-height: 1; letter-spacing: 1px;
    text-align: center;
  }
  .card--front .wordmark { font-size: 58px; }
  .card--back .wordmark { font-size: 34px; }

  .back-brand { width: 330px; display: flex; justify-content: center; }
  .divider { width: 1px; height: 230px; background: var(--rule); }
  .details { padding-left: 36px; color: var(--silver-soft); }
  .person-name { font-size: 27px; font-weight: 500; letter-spacing: 2px; color: var(--silver); }
  .person-role { font-size: 15px; color: var(--muted); margin: 2px 0 20px; }
  .address { font-size: 17px; line-height: 1.35; margin-bottom: 14px; }
  .contact-line { display: flex; align-items: center; gap: 10px; font-size: 17px; line-height: 1.5; }
  .contact-line svg { width: 13px; height: 13px; flex: none; }
  .contact-line.plain { padding-left: 23px; }
</style>
</head>
<body>
<main class="canvas">
  <section class="card card--front">
    <div class="wordmark">Korvan<br>Builders, Inc.</div>
  </section>

  <section class="card card--back">
    <div class="back-brand">
      <div class="wordmark">Korvan<br>Builders, Inc.</div>
    </div>
    <div class="divider"></div>
    <div class="details">
      <div class="person-name">DANIEL MERCER</div>
      <div class="person-role">Director</div>
      <div class="address">418 Harbor Ave.<br>Linden, NJ 07036</div>
      <div class="contact-line">
        <svg viewBox="0 0 16 16" fill="var(--silver-soft)"><path d="M3.5 1.5l2.5 0 1 3.5-1.6 1.2a9 9 0 0 0 4.4 4.4l1.2-1.6 3.5 1v2.5c0 .8-.7 1.5-1.5 1.5C6.7 14 2 9.3 2 3c0-.8.7-1.5 1.5-1.5z"/></svg>
        <span>(908) 555-0147</span>
      </div>
      <div class="contact-line">
        <svg viewBox="0 0 16 16" fill="none" stroke="var(--silver-soft)" stroke-width="1.4"><rect x="1.5" y="3.5" width="13" height="9" rx="1"/><path d="M1.5 4l6.5 5 6.5-5"/></svg>
        <span>info@korvanbuilders.com</span>
      </div>
      <div class="contact-line">
        <svg viewBox="0 0 16 16" fill="none" stroke="var(--silver-soft)" stroke-width="1.3"><circle cx="8" cy="8" r="6.5"/><ellipse cx="8" cy="8" rx="2.8" ry="6.5"/><path d="M1.5 8h13"/></svg>
        <span>www.korvanbuilders.com</span>
      </div>
      <div class="contact-line plain">www.korvanbuilders.com</div>
    </div>
  </section>
</main>
</body>
</html>
```